'Cradle Ahead' promotional brochure

We have designed a 6 week program to educate impending first-time parents about the things they need to know to survive the first 6 months. Sessions delivered by general practitioner/family doctor, dietician, physiotherapist, speech pathologist and psychologist. Our promotional blurb is: 'A comprehensive education program for first-time parents-to-be, delivered over 6 weeks by health professionals in your community, about everything you need to know to look after your baby (and yourself!) in the first 6 months'. I now want to put together a promotional brochure to be distributed to those couples who express an interest which will provide further details of what will be delivered in the course.
Updates
In terms of layout, I envisaged a double sided A4 size, foldable into 3 sections, but very happy to be guided on this.
Target Market(s)
To appeal to a young, well educated demographic. First time parents couples.
Industry/Entity Type
Medical
Font styles to use
Other font styles liked:
- Playfair Display
Requirements
Must have
- Playfair display font to be consistent with our logo (attached). Logo also included please. Some consistency with colours of logo please.
Nice to have
- I am a doctor, and have no creative genes! But prefer a clean and professional appearance overall. Not too cluttered in overall appearance.
Should not have
- No cheesy pictures of babies.

```html
<!DOCTYPE html>
<html lang="en">
<head>
<meta charset="utf-8">
<title>Cradle Ahead – Brochure Back Page</title>
<link href="https://fonts.googleapis.com/css2?family=Raleway:wght@300;400;600;700&family=Playfair+Display:wght@400;700&display=swap" rel="stylesheet">
<style>
  :root {
    --lime: #9ccc3d;
    --lime-deep: #7fb52b;
    --lime-pale: #dcefb4;
    --ink: #111111;
    --paper: #ffffff;
    --stage: #c8e497;
  }
  * { margin: 0; padding: 0; box-sizing: border-box; }
  html, body { width: 1200px; height: 1200px; overflow: hidden; }
  body {
    background: radial-gradient(circle at 50% 45%, #eef7de 0%, var(--stage) 60%, #a9d45a 100%);
    font-family: "Raleway", sans-serif;
    position: relative;
  }
  .brochure {
    position: absolute;
    left: 30px; top: 197px;
    width: 1140px; height: 806px;
    display: flex;
    box-shadow: 0 12px 40px rgba(60, 90, 20, 0.25);
  }
  .panel { position: relative; width: 380px; height: 806px; overflow: hidden; }
  .panel--week5 { background: linear-gradient(160deg, var(--lime) 0%, #c4e28a 35%, #eef6de 70%, #f7fbef 100%); }
  .panel--week6 { background: linear-gradient(180deg, #ffffff 0%, #f1f8e3 60%, #e3f0c9 100%); border-left: 1px solid rgba(0,0,0,0.05); }
  .panel--cover { background: var(--paper); border-left: 1px solid rgba(0,0,0,0.05); }

  .panel svg.decor { position: absolute; left: 0; top: 0; }

  .week-tag {
    position: absolute;
    width: 104px; height: 62px;
    border-radius: 50%;
    background: var(--ink);
    color: var(--paper);
    font-weight: 700;
    font-size: 19px;
    display: flex; align-items: center; justify-content: center;
    box-shadow: 0 4px 0 #ffffff, 0 6px 8px rgba(0,0,0,0.2);
    z-index: 2;
  }
  .session-bubble {
    position: absolute;
    border-radius: 50%;
    background: var(--lime);
    color: var(--paper);
    font-size: 13.5px;
    line-height: 1.32;
    font-weight: 400;
    text-align: justify;
  }
  .session-bubble strong { font-weight: 700; }
  .session-bubble p { position: absolute; }
  .session-bubble p + p { margin-top: 0; }

  .panel--week5 .week-tag { left: 58px; top: 40px; }
  .panel--week5 .session-bubble { left: 40px; top: 70px; width: 310px; height: 310px; }
  .panel--week5 .session-bubble p { left: 24px; right: 16px; top: 98px; }

  .panel--week6 .week-tag { left: 42px; top: 265px; }
  .panel--week6 .session-bubble { left: 30px; top: 290px; width: 310px; height: 310px; }
  .panel--week6 .p1 { left: 26px; right: 22px; top: 70px; }
  .panel--week6 .p2 { left: 26px; right: 22px; top: 190px; }

  .photo-area { position: absolute; left: 0; top: 0; }

  .brand {
    position: absolute; left: 118px; top: 52px;
    display: flex; align-items: center; gap: 10px;
    color: var(--lime-deep);
    font-family: "Playfair Display", serif;
    font-size: 13px; line-height: 1.05;
    text-transform: uppercase;
  }
  .brand-mark { width: 34px; height: 34px; background: var(--lime-deep); }

  .cover-title {
    position: absolute; left: 0; right: 0; top: 400px;
    text-align: center;
    font-family: "Raleway", sans-serif;
    font-weight: 700;
    color: var(--lime-deep);
    font-size: 58px; line-height: 0.98;
    text-transform: uppercase;
    letter-spacing: -1px;
  }
  .cover-blurb {
    position: absolute; left: 48px; right: 36px; top: 538px;
    text-align: center;
    font-family: "Playfair Display", serif;
    font-size: 9.5px; line-height: 1.35;
    text-transform: uppercase;
    color: var(--ink);
  }
  .cover-subline {
    position: absolute; left: 40px; right: 30px; top: 585px;
    text-align: center;
    font-family: "Playfair Display", serif;
    font-size: 6.5px; line-height: 1.3;
    text-transform: uppercase;
    color: var(--ink);
  }
  .cover-subline span { color: var(--lime-deep); }
  .enquiries {
    position: absolute; left: 0; right: 0; top: 616px;
    text-align: center;
    font-family: "Playfair Display", serif;
  }
  .enquiries .label { font-size: 10px; color: var(--lime-deep); text-decoration: underline; text-transform: uppercase; }
  .enquiries .phone { font-size: 19px; color: var(--ink); margin-top: 4px; }
  .price {
    position: absolute; right: 46px; top: 730px;
    text-align: center;
    font-family: "Playfair Display", serif;
    color: var(--paper);
    font-size: 18px; line-height: 1.2;
    text-transform: uppercase;
  }
</style>
</head>
<body>
  <main class="brochure">

    <section class="panel panel--week5">
      <svg class="decor" width="380" height="806" viewBox="0 0 380 806" aria-hidden="true">
        <path d="M250 330 Q300 400 360 410 L320 440 Q300 430 280 455 Q300 420 250 330 Z" fill="var(--lime)"/>
        <path d="M0 670 Q160 690 220 790 L225 806 L0 806 Z" fill="var(--lime)"/>
        <path d="M0 690 Q140 705 200 806 L0 806 Z" fill="var(--ink)"/>
      </svg>
      <div class="week-tag">WEEK 5</div>
      <div class="session-bubble">
        <p><strong>Session 1</strong> – Clinical Psychologist <strong>Dr Maren Ellery</strong> will share information about bonding &amp; attachment with your baby, how to promote their social &amp; emotional development and how to manage separation anxiety. She will also discuss positive parenting approaches.</p>
      </div>
    </section>

    <section class="panel panel--week6">
      <div class="week-tag">WEEK 6</div>
      <div class="session-bubble">
        <p class="p1"><strong>Session 1 – Secret Men's Business</strong> – a men-only session (including beer!) with a new father for frank discussion about the road ahead. Mums will do a shopping excursion with the GP &amp; Dietician to Freshway to look at baby products and food – the good and the bad!</p>
        <p class="p2">Session 2 – Program review, reflection and evaluation and future session planning when baby is 6 months of age.</p>
      </div>
    </section>

    <section class="panel panel--cover">
      <svg class="photo-area" width="380" height="806" viewBox="0 0 380 806" role="img" aria-label="Photo of a mother cuddling her baby, tinted lime green">
        <defs>
          <linearGradient id="photoTint" x1="0" y1="0" x2="1" y2="1">
            <stop offset="0" stop-color="#b8dc72"/>
            <stop offset="0.5" stop-color="#a3cf4c"/>
            <stop offset="1" stop-color="#8cc03a"/>
          </linearGradient>
        </defs>
        <path d="M0 0 H380 V255 Q300 300 220 350 Q120 410 60 370 Q20 345 0 300 Z" fill="url(#photoTint)"/>
      </svg>
      <svg class="decor" width="380" height="806" viewBox="0 0 380 806" aria-hidden="true">
        <path d="M0 300 Q20 345 60 370 Q120 410 220 350 Q300 300 380 255 L380 275 Q300 320 225 370 Q120 430 55 392 Q15 365 0 325 Z" fill="var(--ink)"/>
        <path d="M380 615 Q260 660 190 806 L380 806 Z" fill="var(--lime)"/>
        <path d="M380 640 Q280 680 215 806 L380 806 Z" fill="var(--ink)"/>
      </svg>
      <div class="brand">
        <span class="brand-mark"></span>
        <span>Wattle Grove<br>Health &amp;<br>Medical</span>
      </div>
      <h1 class="cover-title">Cradle<br>Ahead</h1>
      <p class="cover-blurb">A comprehensive education program for first-time parents-to-be, delivered over 6 weeks by health professionals in your community.</p>
      <p class="cover-subline">Everything you need to know to look after your baby (and yourself!)<br><span>in the first 6 months.</span></p>
      <div class="enquiries">
        <div class="label">For enquiries:</div>
        <div class="phone">(02) 5550 1234</div>
      </div>
      <div class="price">Only<br>$300.00</div>
    </section>

  </main>
</body>
</html>
```